Charity auction mobile bidding site

Our charities can build their own event landing page to promote their silent auction fundraising event. We need a top menu, hero image with event title and desc, a register/login area, up to 4 content blocks and an auction listing of items in a grid dynamically created from their catalog. Currently we have this laid out in 100% width layers or stacks. It needs to be mobile friendly first. Examples include kpdemo.zuv.io and lindal.zuv.io and bexstest.zuv.io We need to allow people to design nice sites instead of PalNook pages that look terrible.

Target Market(s)

Soccer moms and volunteers who feel like rockstars when they learn how to use linkwave or clipvale. Not super savvy so less is more. Not overwhelming. Clean with whitespace and functional is what they want

Number of Pages Required

1 page

Font styles to use
Sans Serif

Colors

Designer to choose colors to be used in the design.

Requirements
Must have
• Nothing so tightly designed that it would look terrible if an organization loaded their own photos. This means the hero image could be landscape or portrait. When in doubt, keep it clean and simple. A one or two color palette
Nice to have
• A pop up concept for someone to log in when they choose to bid on an item in the preview.
Should not have
• Decorative fonts. Too many colors.

```html
<!DOCTYPE html>
<html lang="en">
<head>
<meta charset="utf-8">
<title>Charity Auction – Mobile Bidding</title>
<link rel="stylesheet" href="https://fonts.googleapis.com/css2?family=Kreon:wght@400;500&family=Noto+Serif:wght@400&family=Arimo&display=swap">
<style>
  :root {
    --canvas: #e4e4e4;
    --white: #ffffff;
    --accent: #ff5a0a;
    --muted-btn: #6e6e6e;
    --dark-btn: #454545;
    --ink: #333333;
    --body-text: #666666;
    --line: #ececec;
    --footer: #222222;
    --overlay: rgba(20, 16, 14, 0.45);
  }
  * { box-sizing: border-box; margin: 0; padding: 0; }
  html, body { width: 1200px; height: 4371px; overflow: hidden; }
  body { background: var(--canvas); font-family: "Noto Serif", serif; color: var(--ink); position: relative; }

  .phone {
    position: absolute; top: 63px; width: 513px; height: 4217px;
    background: var(--white); border-top: 5px solid var(--accent); overflow: hidden;
  }
  .phone--list { left: 59px; }
  .phone--popup { left: 621px; }

  .abs { position: absolute; }
  .center-line { left: 0; width: 100%; text-align: center; }

  /* Header */
  .topbar { top: 0; left: 0; width: 100%; height: 121px; }
  .icon-btn {
    position: absolute; top: 24px; width: 68px; height: 68px; border-radius: 50%;
    border: 2px solid #d8d8d8; display: flex; align-items: center; justify-content: center;
  }
  .icon-btn--search { left: 22px; }
  .icon-btn--menu { left: 422px; }
  .brand { top: 34px; font-family: "Kreon", serif; font-size: 37px; color: var(--ink); line-height: 48px; }

  /* Hero */
  .hero { top: 121px; left: 0; width: 100%; height: 392px;
    background: linear-gradient(120deg, #6b5a4e 0%, #3d3532 35%, #5d4a42 60%, #2e2a2c 100%); }
  .hero-shade { inset: 0; background: var(--overlay); }
  .hero-title { top: 134px; font-family: "Kreon", serif; font-size: 44px; color: var(--white); line-height: 56px; }
  .hero-text { top: 202px; font-size: 17px; line-height: 33px; color: var(--white); }
  .btn {
    position: absolute; display: flex; align-items: center; justify-content: center;
    font-family: "Kreon", serif; color: var(--white); border-radius: 2px;
  }
  .btn--hero { top: 290px; left: 183px; width: 146px; height: 52px; background: var(--accent); font-size: 19px; }

  /* Welcome */
  .section-title { font-family: "Kreon", serif; font-size: 32px; line-height: 42px; color: var(--ink); }
  .rule { position: absolute; left: 224px; width: 65px; height: 2px; background: var(--accent); }
  .welcome-title { top: 564px; }
  .welcome-rule { top: 629px; }
  .welcome-text { top: 663px; left: 24px; width: 465px; text-align: center; font-size: 16.5px; line-height: 34px; color: var(--body-text); }
  .btn--register { top: 835px; left: 68px; width: 176px; height: 60px; background: var(--accent); font-size: 25px; }
  .btn--login { top: 835px; left: 255px; width: 176px; height: 60px; background: var(--muted-btn); font-size: 25px; }
  .divider { top: 947px; left: 0; width: 100%; height: 1px; background: var(--line); }

  /* Auction preview */
  .preview-title { top: 990px; }
  .preview-rule { top: 1057px; }
  .card {
    position: absolute; left: 34px; width: 446px; height: 688px;
    background: var(--white); border: 1px solid #e6e6e6; box-shadow: 0 0 6px rgba(0,0,0,0.06);
  }
  .card-photo { position: absolute; top: 24px; left: 17px; width: 412px; height: 289px; }
  .photo--bidders { background: linear-gradient(135deg, #e9e4e2 0%, #b8c3c6 35%, #3c5560 65%, #d7d2cf 100%); }
  .photo--laptop { background: linear-gradient(120deg, #cfd3cf 0%, #e8e6e2 35%, #c7b3a2 60%, #6f6258 100%); }
  .photo--hands { background: linear-gradient(160deg, #b59d6a 0%, #3a2d28 40%, #c7a898 70%, #221c1f 100%); }
  .photo--cash { background: linear-gradient(140deg, #e9c9a5 0%, #d9ab80 45%, #a9b8ae 70%, #e7c29a 100%); }
  .card-title { top: 352px; font-family: "Kreon", serif; font-size: 27px; line-height: 36px; color: var(--ink); }
  .card-bid { top: 406px; font-family: "Kreon", serif; font-size: 23px; line-height: 30px; color: var(--accent); }
  .card-text { top: 451px; left: 28px; width: 390px; text-align: center; font-size: 16.5px; line-height: 37px; color: var(--body-text); }
  .btn--details { top: 586px; left: 127px; width: 190px; height: 61px; background: var(--accent); font-size: 24px; }
  .btn--details.is-active { background: var(--dark-btn); }

  /* Footer */
  .footer { top: 4056px; left: 0; width: 100%; height: 161px; background: var(--footer); }
  .footer-brand { top: 38px; font-family: "Kreon", serif; font-size: 37px; line-height: 46px; color: var(--white); }
  .footer-copy { top: 102px; font-family: "Arimo", sans-serif; font-size: 16px; line-height: 22px; color: var(--white); }

  /* Popup */
  .bid-popup {
    position: absolute; top: 1273px; left: 20px; width: 470px; height: 395px;
    background: var(--white); border: 2px solid #f08a55; box-shadow: 0 2px 10px rgba(0,0,0,0.12);
  }
  .popup-scroll { position: absolute; top: 4px; right: 4px; width: 10px; height: 383px; border-left: 1px solid #e5e5e5; }
  .popup-close { position: absolute; top: 18px; left: 420px; }
  .popup-title { position: absolute; top: 30px; left: 29px; font-family: "Kreon", serif; font-size: 34px; line-height: 44px; color: var(--ink); }
  .popup-label { position: absolute; left: 29px; font-size: 18px; line-height: 26px; color: var(--ink); }
  .popup-text { position: absolute; left: 29px; width: 410px; font-size: 16px; line-height: 34px; color: var(--body-text); text-align: justify; }
</style>
</head>
<body>

<!-- Screen: auction list -->
<section class="phone phone--list">
  <header class="abs topbar">
    <div class="icon-btn icon-btn--search">
      <svg width="20" height="20" viewBox="0 0 20 20"><circle cx="8" cy="8" r="5.5" fill="none" stroke="#666" stroke-width="2.4"/><line x1="12" y1="12" x2="17" y2="17" stroke="#666" stroke-width="2.6" stroke-linecap="round"/></svg>
    </div>
    <div class="abs center-line brand">Charity Auction</div>
    <div class="icon-btn icon-btn--menu">
      <svg width="20" height="16" viewBox="0 0 20 16"><rect x="1" y="1" width="18" height="2.6" fill="#666"/><rect x="1" y="6.7" width="18" height="2.6" fill="#666"/><rect x="1" y="12.4" width="18" height="2.6" fill="#666"/></svg>
    </div>
  </header>

  <div class="abs hero" role="img" aria-label="Hero photo of an auction gavel held by a bidder">
    <div class="abs hero-shade"></div>
    <h1 class="abs center-line hero-title">Charity Auction</h1>
    <p class="abs center-line hero-text">Sed ut perspiciatis unde omnis iste natus error<br>sit voluptatem accusantium</p>
    <a class="btn btn--hero">Read More</a>
  </div>

  <h2 class="abs center-line section-title welcome-title">Welcome Charity Auction</h2>
  <div class="rule welcome-rule"></div>
  <p class="abs welcome-text">Sed ut perspiciatis unde omnis iste natus error sit voluptatem accusantium doloremque laudantium, totam rem aperiam, eaque ipsa quae ab illo inventore veritatis et architecto beatae vitae dicta sunt explicabo.</p>
  <a class="btn btn--register">Register</a>
  <a class="btn btn--login">Login</a>
  <div class="abs divider"></div>

  <h2 class="abs center-line section-title preview-title">Auction Preview</h2>
  <div class="rule preview-rule"></div>

  <article class="card" style="top:1101px">
    <div class="card-photo photo--bidders" role="img" aria-label="Photo of a room of people raising bid paddles"></div>
    <h3 class="abs center-line card-title">Sed ut perspiciatis unde</h3>
    <p class="abs center-line card-bid">Current Bid: $700</p>
    <p class="abs card-text">Sed ut perspiciatis unde omnis iste natus error sit voluptatem accusantium doloremque laud antium, totam rem aperiam</p>
    <a class="btn btn--details is-active">View Details</a>
  </article>
  <article class="card" style="top:1838px">
    <div class="card-photo photo--laptop" role="img" aria-label="Photo of a couple bidding excitedly on a laptop"></div>
    <h3 class="abs center-line card-title">Sed ut perspiciatis unde</h3>
    <p class="abs center-line card-bid">Current Bid: $700</p>
    <p class="abs card-text">Sed ut perspiciatis unde omnis iste natus error sit voluptatem accusantium doloremque laud antium, totam rem aperiam</p>
    <a class="btn btn--details">View Details</a>
  </article>
  <article class="card" style="top:2574px">
    <div class="card-photo photo--hands" role="img" aria-label="Photo of raised hands in a crowd"></div>
    <h3 class="abs center-line card-title">Sed ut perspiciatis unde</h3>
    <p class="abs center-line card-bid">Current Bid: $700</p>
    <p class="abs card-text">Sed ut perspiciatis unde omnis iste natus error sit voluptatem accusantium doloremque laud antium, totam rem aperiam</p>
    <a class="btn btn--details">View Details</a>
  </article>
  <article class="card" style="top:3311px">
    <div class="card-photo photo--cash" role="img" aria-label="Photo of hands beside stacks of banknotes on a desk"></div>
    <h3 class="abs center-line card-title">Sed ut perspiciatis unde</h3>
    <p class="abs center-line card-bid">Current Bid: $700</p>
    <p class="abs card-text">Sed ut perspiciatis unde omnis iste natus error sit voluptatem accusantium doloremque laud antium, totam rem aperiam</p>
    <a class="btn btn--details">View Details</a>
  </article>

  <footer class="abs footer">
    <div class="abs center-line footer-brand">Charity Auction</div>
    <p class="abs center-line footer-copy">© Copyright 2020 Charity Auction.All right reserved</p>
  </footer>
</section>

<!-- Screen: item details popup -->
<section class="phone phone--popup">
  <header class="abs topbar">
    <div class="icon-btn icon-btn--search">
      <svg width="20" height="20" viewBox="0 0 20 20"><circle cx="8" cy="8" r="5.5" fill="none" stroke="#666" stroke-width="2.4"/><line x1="12" y1="12" x2="17" y2="17" stroke="#666" stroke-width="2.6" stroke-linecap="round"/></svg>
    </div>
    <div class="abs center-line brand">Charity Auction</div>
    <div class="icon-btn icon-btn--menu">
      <svg width="20" height="16" viewBox="0 0 20 16"><rect x="1" y="1" width="18" height="2.6" fill="#666"/><rect x="1" y="6.7" width="18" height="2.6" fill="#666"/><rect x="1" y="12.4" width="18" height="2.6" fill="#666"/></svg>
    </div>
  </header>

  <div class="abs hero" role="img" aria-label="Hero photo of an auction gavel held by a bidder">
    <div class="abs hero-shade"></div>
    <h1 class="abs center-line hero-title">Charity Auction</h1>
    <p class="abs center-line hero-text">Sed ut perspiciatis unde omnis iste natus error<br>sit voluptatem accusantium</p>
    <a class="btn btn--hero">Read More</a>
  </div>

  <h2 class="abs center-line section-title welcome-title">Welcome Charity Auction</h2>
  <div class="rule welcome-rule"></div>
  <p class="abs welcome-text">Sed ut perspiciatis unde omnis iste natus error sit voluptatem accusantium doloremque laudantium, totam rem aperiam, eaque ipsa quae ab illo inventore veritatis et architecto beatae vitae dicta sunt explicabo.</p>
  <a class="btn btn--register">Register</a>
  <a class="btn btn--login">Login</a>
  <div class="abs divider"></div>

  <h2 class="abs center-line section-title preview-title">Auction Preview</h2>
  <div class="rule preview-rule"></div>

  <article class="card" style="top:1101px">
    <div class="card-photo photo--bidders" role="img" aria-label="Photo of a room of people raising bid paddles"></div>
    <h3 class="abs center-line card-title">Sed ut perspiciatis unde</h3>
    <p class="abs center-line card-bid">Current Bid: $700</p>
    <p class="abs card-text">Sed ut perspiciatis unde omnis iste natus error sit voluptatem accusantium doloremque laud antium, totam rem aperiam</p>
    <a class="btn btn--details is-active">View Details</a>
  </article>
  <article class="card" style="top:1838px">
    <div class="card-photo photo--laptop" role="img" aria-label="Photo of a couple bidding excitedly on a laptop"></div>
    <h3 class="abs center-line card-title">Sed ut perspiciatis unde</h3>
    <p class="abs center-line card-bid">Current Bid: $700</p>
    <p class="abs card-text">Sed ut perspiciatis unde omnis iste natus error sit voluptatem accusantium doloremque laud antium, totam rem aperiam</p>
    <a class="btn btn--details">View Details</a>
  </article>
  <article class="card" style="top:2574px">
    <div class="card-photo photo--hands" role="img" aria-label="Photo of raised hands in a crowd"></div>
    <h3 class="abs center-line card-title">Sed ut perspiciatis unde</h3>
    <p class="abs center-line card-bid">Current Bid: $700</p>
    <p class="abs card-text">Sed ut perspiciatis unde omnis iste natus error sit voluptatem accusantium doloremque laud antium, totam rem aperiam</p>
    <a class="btn btn--details">View Details</a>
  </article>
  <article class="card" style="top:3311px">
    <div class="card-photo photo--cash" role="img" aria-label="Photo of hands beside stacks of banknotes on a desk"></div>
    <h3 class="abs center-line card-title">Sed ut perspiciatis unde</h3>
    <p class="abs center-line card-bid">Current Bid: $700</p>
    <p class="abs card-text">Sed ut perspiciatis unde omnis iste natus error sit voluptatem accusantium doloremque laud antium, totam rem aperiam</p>
    <a class="btn btn--details">View Details</a>
  </article>

  <div class="bid-popup" role="dialog" aria-label="Item details">
    <div class="popup-scroll">
      <svg width="10" height="383" viewBox="0 0 10 383"><path d="M5 4 L8 8 L2 8 Z" fill="#999"/><path d="M5 379 L8 375 L2 375 Z" fill="#999"/></svg>
    </div>
    <svg class="popup-close" width="22" height="22" viewBox="0 0 22 22"><circle cx="11" cy="11" r="10" fill="#111"/><path d="M7 7 L15 15 M15 7 L7 15" stroke="#fff" stroke-width="2.6" stroke-linecap="round"/></svg>
    <h3 class="popup-title">Sed ut perspiciatis unde</h3>
    <p class="popup-label" style="top:97px">Details:</p>
    <p class="popup-text" style="top:130px">Sed ut perspiciatis unde omnis iste natus error sit beatae vitae dicta sunt explicabo.</p>
    <p class="popup-label" style="top:219px">Exceptions:</p>
    <p class="popup-text" style="top:252px">Sed ut perspiciatis unde omnis iste natus</p>
    <p class="popup-label" style="top:300px">Donated by :</p>
    <p class="popup-text" style="top:333px">Mara Quill</p>
  </div>

  <footer class="abs footer">
    <div class="abs center-line footer-brand">Charity Auction</div>
    <p class="abs center-line footer-copy">© Copyright 2020 Charity Auction.All right reserved</p>
  </footer>
</section>

</body>
</html>
```